Verpackungen für Matcha Tee Sticks
Zielgruppe
Premium Matcha Tee Sticks in hochwertiger Qualität. Die Umverpackung wird voraussichtlich in Dosen sein.
Unsere Zielgruppe sind Menschen mit Lust auf guten Geschmack und eine Prise Luxus, ReisSportler, Gesundheitsbewusste und Genießer.
Aufgabenstellung
Wir brauchen ein Logo & eine Verpackung (Banderole) für Dosen (Durchmesser: 63/ Höhe: 105 mm) für unser Label 'teefix4go'.
Modern, Luxuriös, Schlicht - Farben: gold, grün, schwarz, weiß (sind aber auch für andere Farbvarianten offen)
Die Matcha Sticks werden wahrscheinlich in schwarzen oder weißen oder goldenen Dosen verkauft werden.
Abmessungen Banderole: ca. Höhe: 105 / Breite:178mm
@all: Tendenziell sollen die Vorschläge noch luxuriöser und feiner werden. z.B. schwarzer Hintergrund mit feiner Schrift oder z.B. die Marke QRP Brew aus Singapur hat erlesene Tees in luxuriösem Design. Inspirierende Marken: Belnoix Vamont (Kekse, Kerzen), Ulla Verbeck (Kosmetik), Tissand Oulmes (Tee), Brevo oder ZAR Tee....
Es darf gerne ein Eyecatcher sein, IT-piece, must-have.... Eine Dose, die man lieber sammelt als nach Gebrauch wegzuschmeißen. Ihr könnt Euch auch vom Farbschema lösen. Das war nur ein erster Gedanke, da Matcha grün ist und die Dose voraussichtlich schwarz und gold Luxus verkörpert. Stellt Euch die Einkaufsmall in Dubai vor. Da heißt es auffallen. Knallorange....es muss rocken.
Wir sind gespannt auf weitere Vorschläge und möchten uns auch für die eingegangen Vorschläge bedanken. Wir wissen, dass da schon einiges an Arbeit drinsteckt.
Happy Weekend :)

```html
<!DOCTYPE html>
<html lang="de">
<head>
<meta charset="utf-8">
<title>teefix4go – Banderolen Matcha Tee Sticks</title>
<link rel="stylesheet" href="https://fonts.googleapis.com/css2?family=Merriweather:wght@400;700&display=swap">
<style>
  :root {
    --canvas: #ffffff;
    --label-black: #000000;
    --orange: #f7a000;
    --orange-deep: #e08a00;
    --gold-light: #f6dc93;
    --gold: #d9a441;
    --gold-deep: #a8741c;
    --crackle-dark: #1a1205;
    --crackle-mid: #4a3410;
  }
  * { box-sizing: border-box; margin: 0; padding: 0; }
  html, body { width: 1200px; height: 1200px; overflow: hidden; background: var(--canvas); }
  body { position: relative; font-family: "Merriweather", Georgia, serif; }

  .banderole {
    position: absolute;
    left: 120px;
    width: 960px;
    height: 566px;
    background: var(--label-black);
    overflow: hidden;
  }
  .banderole--orange { top: 24px; --accent: var(--orange); }
  .banderole--gold { top: 610px; --accent: var(--gold); }

  .crackle-texture {
    position: absolute;
    left: 0; right: 0; bottom: 0;
    height: 190px;
    background: linear-gradient(to bottom, rgba(0,0,0,0) 0%, var(--crackle-dark) 35%, var(--crackle-mid) 100%);
    opacity: 0.9;
  }
  .speckle-texture {
    position: absolute;
    inset: 0;
    background: radial-gradient(ellipse at 30% 25%, rgba(90,60,15,0.35), rgba(0,0,0,0) 45%),
                radial-gradient(ellipse at 80% 40%, rgba(90,60,15,0.3), rgba(0,0,0,0) 40%);
  }

  .info-text {
    position: absolute;
    left: 20px;
    width: 130px;
    font-size: 7.6px;
    line-height: 14px;
    font-weight: 700;
    color: var(--accent);
  }
  .info-text--first { top: 122px; }
  .info-text--second { top: 282px; }
  .banderole--gold .info-text { color: var(--gold-light); font-weight: 400; }

  .emblem { position: absolute; left: 265px; top: 70px; width: 430px; height: 360px; }

  .brand-name {
    position: absolute;
    left: 0; right: 0;
    top: 110px;
    text-align: center;
    font-size: 24px;
    font-weight: 700;
    letter-spacing: 3px;
    color: var(--accent);
  }
  .banderole--gold .brand-name { color: var(--gold-light); }

  .illustration {
    position: absolute;
    left: 325px; top: 150px;
    width: 320px; height: 255px;
    border-radius: 40% 40% 30% 30%;
  }
  .banderole--orange .illustration { background: radial-gradient(ellipse at 50% 45%, var(--orange) 0%, var(--orange-deep) 35%, rgba(0,0,0,0) 70%); }
  .banderole--gold .illustration { background: radial-gradient(ellipse at 50% 45%, var(--gold-light) 0%, var(--gold) 35%, rgba(0,0,0,0) 70%); }

  .product-title {
    position: absolute;
    left: 0; right: 0;
    top: 430px;
    text-align: center;
    font-size: 24px;
    font-weight: 700;
    letter-spacing: 2px;
    color: var(--accent);
  }
  .banderole--gold .product-title { color: var(--gold-light); font-weight: 400; }
  .title-rule {
    position: absolute;
    left: 318px; width: 322px;
    top: 471px;
    height: 1.5px;
    background: var(--accent);
  }
  .product-claim {
    position: absolute;
    left: 0; right: 0;
    top: 481px;
    text-align: center;
    font-size: 12.5px;
    font-weight: 700;
    letter-spacing: 1px;
    color: var(--accent);
  }
  .banderole--gold .product-claim { color: var(--gold-light); font-weight: 400; }

  .contents-note {
    position: absolute;
    left: 840px;
    top: 408px;
    font-size: 9px;
    line-height: 14px;
    color: var(--accent);
  }
  .banderole--gold .contents-note { color: var(--gold-light); }
</style>
</head>
<body>

<section class="banderole banderole--orange" aria-label="Banderole Variante Orange">
  <p class="info-text info-text--first">Lorem ipsum dolor sit amet, consectetuer adipiscing elit. Aenean commodo ligula eget dolor. Aenean massa. Cum sociis natoque penatibus et magnis dis parturient montes, nascetur ridiculus mus. Donec quam felis, ultricies nec, pellentesque eu, pretium quis, sem.</p>
  <p class="info-text info-text--second">Lorem ipsum dolor sit amet, consectetuer adipiscing elit. Aenean commodo ligula eget dolor. Aenean massa. Cum sociis natoque penatibus et magnis dis parturient montes, nascetur ridiculus mus. Donec quam felis, ultricies nec, pellentesque eu, pretium quis, sem. Nulla consequat massa quis enim.</p>

  <svg class="emblem" viewBox="0 0 430 360" aria-hidden="true">
    <path d="M 55 350 A 205 205 0 1 1 375 350" fill="none" stroke="var(--orange)" stroke-width="4"/>
  </svg>
  <p class="brand-name">TEEFIX 4GO</p>
  <div class="illustration" role="img" aria-label="Illustration: Frau im Kimono mit Kirschblüten, Teebesen und Matcha-Schale"></div>

  <h1 class="product-title">MATCHA TEE STICKS</h1>
  <div class="title-rule"></div>
  <p class="product-claim">IN HOCHWERTIGER QUALITÄT</p>

  <p class="contents-note">10 Matcha Sticks<br>je 15g Einwaage</p>
</section>

<section class="banderole banderole--gold" aria-label="Banderole Variante Gold">
  <div class="speckle-texture" role="img" aria-label="Feine goldene Sprenkel-Struktur im Hintergrund"></div>
  <div class="crackle-texture" role="img" aria-label="Goldenes Craquelé-Muster am unteren Rand"></div>

  <p class="info-text info-text--first">Lorem ipsum dolor sit amet, consectetuer adipiscing elit. Aenean commodo ligula eget dolor. Aenean massa. Cum sociis natoque penatibus et magnis dis parturient montes, nascetur ridiculus mus. Donec quam felis, ultricies nec, pellentesque eu, pretium quis, sem.</p>
  <p class="info-text info-text--second">Lorem ipsum dolor sit amet, consectetuer adipiscing elit. Aenean commodo ligula eget dolor. Aenean massa. Cum sociis natoque penatibus et magnis dis parturient montes, nascetur ridiculus mus. Donec quam felis, ultricies nec, pellentesque eu, pretium quis, sem. Nulla consequat massa quis enim.</p>

  <svg class="emblem" viewBox="0 0 430 360" aria-hidden="true">
    <defs>
      <linearGradient id="gold-ring" x1="0" y1="0" x2="1" y2="1">
        <stop offset="0" stop-color="#f6dc93"/>
        <stop offset="0.5" stop-color="#d9a441"/>
        <stop offset="1" stop-color="#a8741c"/>
      </linearGradient>
    </defs>
    <path d="M 55 350 A 205 205 0 1 1 375 350" fill="none" stroke="url(#gold-ring)" stroke-width="4"/>
  </svg>
  <p class="brand-name">TEEFIX 4GO</p>
  <div class="illustration" role="img" aria-label="Illustration in Gold: Frau im Kimono mit Kirschblüten, Teebesen und Matcha-Schale"></div>

  <h2 class="product-title">MATCHA TEE STICKS</h2>
  <div class="title-rule"></div>
  <p class="product-claim">IN HOCHWERTIGER QUALITÄT</p>

  <p class="contents-note">10 Matcha Sticks<br>je 15g Einwaage</p>
</section>

</body>
</html>
```